Design Invitation using a mobile phone screen image

This invitation is for 12 year olds finishing primary school so make it fun and bright.
Invitation should be an kavrel with a text message saying.....
Dress in your best (insert emoticons - boy in long pants/girl in dress) for your Year 6 farewell dinner (insert emoticon with tear) on Monday 12 December at 6 pm (insert emoticons - party hat, thumbs up and bowl of icecream). Going 2b a gr8 night!
rsvp YES PLEASE and your name to 0459XXXXXXX

Target Market(s)

12/13 years old boys and girls

Industry/Entity Type

School

Requirements
Must have
• Must be bright and look like a text message - it can have an artwork within it as if the invite has been texted and then a comment is made after the image.
• Must us an kavrel screen as the invitation but so we dont have to cut it out it can be a rectanglar card

```html
<!DOCTYPE html>
<html lang="en">
<head>
<meta charset="utf-8">
<title>Year 6 Farewell Dinner Invitation</title>
<link rel="stylesheet" href="https://fonts.googleapis.com/css2?family=Arimo:wght@400;700&display=swap">
<style>
  :root {
    --party-purple: #5a2a86;
    --party-purple-deep: #3f1c66;
    --party-pink: #e44c9a;
    --party-yellow: #f4c63c;
    --party-blue: #4fb3e6;
    --phone-teal: #3ec6b3;
    --phone-teal-dark: #2aa896;
    --screen-white: #ffffff;
    --screen-grey: #ececec;
    --bar-grey: #d6d6d6;
    --bar-dark: #4a4a4a;
    --line: #9a9a9a;
    --ink: #1e1e1e;
  }
  * { box-sizing: border-box; margin: 0; padding: 0; }
  html, body { width: 826px; height: 1200px; overflow: hidden; }
  body { font-family: "Arimo", Arial, sans-serif; color: var(--ink); }

  .invite { position: relative; width: 826px; height: 1200px; overflow: hidden; }

  .party-backdrop {
    position: absolute; inset: 0;
    background:
      radial-gradient(circle at 12% 20%, var(--party-pink) 0 90px, transparent 140px),
      radial-gradient(circle at 88% 12%, var(--party-yellow) 0 70px, transparent 120px),
      radial-gradient(circle at 90% 55%, var(--party-blue) 0 80px, transparent 130px),
      radial-gradient(circle at 8% 70%, var(--party-yellow) 0 70px, transparent 120px),
      radial-gradient(circle at 85% 88%, var(--party-pink) 0 60px, transparent 110px),
      radial-gradient(ellipse at 50% 45%, var(--party-purple) 0%, var(--party-purple-deep) 100%);
  }

  .phone {
    position: absolute; left: 130px; top: 55px; width: 565px; height: 1100px;
    background: var(--phone-teal);
    border-radius: 72px;
    box-shadow: inset 0 0 0 6px var(--phone-teal-dark);
  }
  .phone-speaker {
    position: absolute; left: 50%; top: 82px; width: 120px; height: 12px;
    transform: translateX(-50%); border-radius: 6px; background: var(--phone-teal-dark);
  }
  .phone-home {
    position: absolute; left: 50%; top: 912px; width: 104px; height: 104px;
    transform: translateX(-50%); border-radius: 50%;
    border: 5px solid var(--phone-teal-dark);
  }

  .screen {
    position: absolute; left: 57px; top: 171px; width: 452px; height: 751px;
    background: var(--screen-white); display: flex; flex-direction: column;
    border: 2px solid var(--phone-teal-dark);
  }
  .nav-bar {
    height: 63px; background: linear-gradient(#f2f2f2, var(--bar-grey));
    display: flex; align-items: center; justify-content: space-between; padding: 0 16px;
    border-bottom: 2px solid var(--line);
  }
  .back-button {
    font-size: 14px; color: #777; padding: 8px 20px; border-radius: 6px;
    background: linear-gradient(#fff, #e0e0e0); border: 1px solid #aaa;
  }
  .menu-icon { width: 36px; height: 24px; }

  .message {
    border-bottom: 2px solid var(--line);
    font-size: 26px; line-height: 1.2; padding: 12px 14px;
  }
  .message-dress { height: 193px; }
  .message-dinner { height: 118px; text-align: center; }
  .message-date { height: 171px; position: relative; }
  .message-rsvp { height: 165px; background: var(--screen-grey); font-size: 24px; }

  .emoji { display: block; border-radius: 50%; }
  .emoji-kids {
    width: 150px; height: 110px; margin: 14px auto 0; border-radius: 30px;
    background: linear-gradient(90deg, #7cb6e8 0 50%, #f08fb8 50% 100%);
  }
  .emoji-tear {
    width: 52px; height: 52px; margin: 8px auto 0;
    background: radial-gradient(circle at 40% 35%, #ffe07a, #f3b52c);
  }
  .emoji-row {
    position: absolute; left: 180px; top: 70px; display: flex; gap: 8px; align-items: flex-end;
  }
  .emoji-hat { width: 62px; height: 84px; border-radius: 10px; background: linear-gradient(#f7a13c, #e8662b); }
  .emoji-thumb { width: 70px; height: 74px; border-radius: 18px; background: linear-gradient(#ffd55a, #f0a92a); }
  .emoji-icecream { width: 70px; height: 84px; border-radius: 34px 34px 12px 12px; background: linear-gradient(#f6b5c9 0 55%, #e3b27a 55%); }

  .search-bar {
    margin-top: auto; height: 41px; background: var(--bar-dark);
    display: flex; align-items: center; justify-content: center;
  }
  .search-field {
    width: 300px; height: 24px; border-radius: 12px; background: #f4f4f4;
    font-size: 12px; color: #999; display: flex; align-items: center; justify-content: center; position: relative;
  }
  .search-field svg { position: absolute; right: 10px; top: 5px; }
</style>
</head>
<body>
<main class="invite">
  <div class="party-backdrop" role="img" aria-label="Purple party backdrop with balloons, streamers and confetti"></div>

  <div class="phone">
    <div class="phone-speaker"></div>

    <section class="screen">
      <header class="nav-bar">
        <span class="back-button">GO BACK</span>
        <svg class="menu-icon" viewBox="0 0 36 24" aria-hidden="true">
          <rect y="0" width="36" height="4" fill="#888"/>
          <rect y="10" width="36" height="4" fill="#888"/>
          <rect y="20" width="36" height="4" fill="#888"/>
        </svg>
      </header>

      <div class="message message-dress">
        <p>Dress in your best</p>
        <span class="emoji emoji-kids" role="img" aria-label="Emoticons of a boy in long pants and a girl in a dress"></span>
      </div>

      <div class="message message-dinner">
        <p>For your Year 6 farewell dinner</p>
        <span class="emoji emoji-tear" role="img" aria-label="Emoticon face with a tear"></span>
      </div>

      <div class="message message-date">
        <p>On Monday 12 December<br>at 6:00 PM</p>
        <div class="emoji-row">
          <span class="emoji emoji-hat" role="img" aria-label="Party hat emoticon"></span>
          <span class="emoji emoji-thumb" role="img" aria-label="Thumbs up emoticon"></span>
          <span class="emoji emoji-icecream" role="img" aria-label="Bowl of ice cream emoticon"></span>
        </div>
      </div>

      <div class="message message-rsvp">
        <p>Going 2b a gr8 night!<br>rsvp<br>YES PLEASE and your name to<br>0459XXXXXXX</p>
      </div>

      <footer class="search-bar">
        <div class="search-field">Search contacts
          <svg width="14" height="14" viewBox="0 0 14 14" aria-hidden="true">
            <circle cx="8" cy="6" r="4" fill="none" stroke="#666" stroke-width="1.6"/>
            <line x1="5" y1="9" x2="1.5" y2="12.5" stroke="#666" stroke-width="1.6"/>
          </svg>
        </div>
      </footer>
    </section>

    <div class="phone-home"></div>
  </div>
</main>
</body>
</html>
```